Web Design Project

We need web design for a new baby products (nursery furniture) business in Australia.

The logo is already done, and I would like to reflect a similar theme throughout the website:
* Clean, white background.
* Use of lime green, purple and orange.
* Similar font to logo for headings
* FUNKY, FASHIONABLE, QUALITY feeling of website.

The main concept is to be attractive to discerning mums who are buying big items like a cot or chest of drawers. These are expensive items and will be considered the most important purchases for a newborn, so the website has to be enticing!!!
Updates

Hello,

Thank you for your submissions. I have received a few questions regarding the font and the coding of this website.

The job I am seeking is for design for an E-commerce store. The font was done by another craft hive designer, so I do not know what type of font I am sorry.

I was hoping to have more designs by now, so please send them soon, this project is guaranteed!

I also ask you to read the brief properly please. The name of the business is Cradle Lane, as the logo says. The use of design that I have mentioned has only been demonstrated in a couple of designs submitted to me.

I look forward to seeing your work soon!

Kind Regards
Marla

Target Market(s)

Young mothers aged 25-45

Industry/Entity Type

Business

Requirements
Must have
• Must be funky, bright, energetic, attractive visually.
Nice to have
• I like the idea of some floral / design work in faded lime green, purple on some of the edges of different pages. Maybe islamic design? But has to be very fashionable.
Should not have
• Should not have any traditional ideas of baby websites.

ie- no stork, nappy images, teddybears etc.

```html
<!DOCTYPE html>
<html lang="en">
<head>
<meta charset="utf-8">
<title>Cradle Lane – Nursery Furniture</title>
<link href="https://fonts.googleapis.com/css2?family=Ubuntu:wght@300;400;500;700&family=Permanent+Marker&family=Covered+By+Your+Grace&display=swap" rel="stylesheet">
<style>
:root{
  --frame:#000000;
  --site-bg:#eef3df;
  --nav-bg:#e7e7e7;
  --white:#ffffff;
  --ink:#222222;
  --grey-text:#666666;
  --cyan:#33bcd8;
  --lime:#8fca12;
  --purple:#c24fe0;
  --plan:#cf5ae6;
  --shop:#8fcb14;
  --support:#f3c90d;
  --connect:#60ae8e;
  --accent-yellow:#f7f23a;
  --thumb-ring:#4a6412;
}
*{margin:0;padding:0;box-sizing:border-box}
html,body{width:1200px;height:900px;overflow:hidden;background:var(--frame);font-family:"Ubuntu",sans-serif}
.site{position:absolute;left:54px;top:12px;width:1094px;height:875px;background:var(--site-bg);
  background-image:radial-gradient(rgba(160,180,120,.18) 1px,transparent 1px);background-size:4px 4px;overflow:hidden}
.topbar{position:absolute;left:0;top:0;width:100%;height:46px;background:var(--nav-bg)}
.nav{position:absolute;top:0;left:569px;display:flex;height:46px;list-style:none}
.nav li{font-size:18px;color:var(--ink);line-height:46px;padding:0 14px;margin-right:10px}
.nav li.active{background:var(--lime);margin-right:10px}
.page{position:absolute;left:109px;top:46px;width:876px;height:743px;background:var(--white);box-shadow:0 3px 8px rgba(0,0,0,.35)}
.brand{position:absolute;left:49px;top:42px;display:flex;align-items:center;gap:14px}
.brand-mark{width:40px;height:40px;border-radius:50%;background:var(--lime)}
.brand-name{font-size:46px;font-weight:700;color:var(--purple);line-height:1}
.fact-photo,.hero-photo,.card-photo,.thumb{position:absolute}
.fact-photo{left:673px;top:46px;width:166px;height:102px;border-radius:48px 60px 50px 40px;background:linear-gradient(135deg,#f2f2f2,#dcdcdc)}
.hero-photo{left:205px;top:160px;width:130px;height:134px;border-radius:40% 45% 30% 35%;background:radial-gradient(circle at 45% 40%,#f6c6dc,#e39bbd 70%,#d8d2c0)}
.fact-title{position:absolute;left:391px;top:76px;font-family:"Permanent Marker",cursive;font-size:32px;color:#5d5d5d;line-height:1}
.fact-sub{position:absolute;left:391px;top:121px;font-size:10px;color:var(--cyan)}
.fact-text{position:absolute;left:391px;top:146px;width:460px;font-size:20px;line-height:24.5px;color:var(--grey-text)}
.fact-text b{font-weight:700}
.fact-text .hl{color:var(--cyan)}
.pager{position:absolute;top:227px;display:flex;gap:6px;left:772px}
.pager svg{display:block}
.card{position:absolute;top:278px;width:188px;height:387px;border-radius:14px;color:var(--white)}
.card h2{position:absolute;left:0;right:0;top:38px;text-align:center;font-weight:400;font-size:40px;line-height:1}
.card .rule{position:absolute;left:29px;right:22px;top:91px;border-top:1px dashed rgba(255,255,255,.9)}
.card.plan{left:35px;background:var(--plan)}
.card.plan h2{text-align:left;left:27px}
.card.shop{left:242px;background:var(--shop)}
.card.shop h2{text-align:left;left:23px}
.card.support{left:444px;background:var(--support)}
.card.connect{left:652px;background:var(--connect)}
.more{position:absolute;left:29px;bottom:23px;width:57px;height:26px;background:var(--white);color:var(--purple);font-size:13px;line-height:26px;text-align:center}
.plan-list{position:absolute;left:29px;top:117px;width:142px;font-size:10.5px;line-height:12.4px}
.plan-list h3{font-size:12px;font-weight:400;color:var(--accent-yellow);margin-bottom:1px}
.plan-list p{margin-bottom:12px}
.shop-label{position:absolute;font-size:12px;line-height:15px;color:var(--white)}
.thumb{width:60px;height:60px;border-radius:50%;border:4px solid var(--thumb-ring)}
.support-list{position:absolute;left:20px;top:113px;width:155px;text-align:center;font-size:10px;line-height:12.5px}
.support-list h3{font-family:"Covered By Your Grace",cursive;font-weight:400;font-size:14px;color:var(--purple);margin-bottom:1px}
.support-list p{margin-bottom:23px}
.script{position:absolute;left:0;right:0;text-align:center;font-family:"Covered By Your Grace",cursive;font-size:18px;color:var(--accent-yellow)}
.social-box{position:absolute;left:26px;top:145px;width:141px;height:59px;background:var(--white);display:flex;flex-direction:column;justify-content:center;align-items:center;gap:2px}
.social-box span{font-size:9.5px;color:var(--grey-text)}
.field{position:absolute;left:26px;width:141px;height:17px;background:var(--white);color:var(--ink);font-size:9.5px;line-height:17px;padding-left:11px}
.subscribe{position:absolute;right:20px;top:307px;font-family:"Covered By Your Grace",cursive;font-size:14px;color:var(--accent-yellow)}
.footer{position:absolute;left:743px;top:828px;font-size:9.5px;line-height:12px;color:#444}
.footer a{color:#888;text-decoration:underline}
.footer-social{position:absolute;left:929px;top:829px;display:flex;gap:4px}
.footer-social span{display:block;width:22px;height:22px;font-size:0}
.footer-social .dark{background:#333}
.footer-social .light{background:#999}
</style>
</head>
<body>
<div class="site">
  <div class="topbar">
    <ul class="nav">
      <li class="active">about us</li>
      <li>products</li>
      <li>shop</li>
      <li>contact us</li>
    </ul>
  </div>

  <div class="page">
    <div class="brand">
      <span class="brand-mark"></span>
      <span class="brand-name">Cradle Lane</span>
    </div>

    <div class="hero-photo" role="img" aria-label="Pink floral baby car seat"></div>
    <div class="fact-photo" role="img" aria-label="Sketched thought bubble with question marks"></div>

    <div class="fact-title">DID you KNOW?</div>
    <div class="fact-sub">Lorem ipsum dolor sit amet.</div>
    <p class="fact-text"><b>Lorem ipsum</b> dolor sit amet. Lorem ipsum dolor sit amet. Lorem ipsum dolor <span class="hl">sit amet.</span>&nbsp; Lorem ipsum dolor sit amet.</p>

    <div class="pager">
      <svg width="23" height="23" viewBox="0 0 23 23" aria-label="Previous"><circle cx="11.5" cy="11.5" r="10.5" fill="none" stroke="#777" stroke-width="1.5"/><path d="M11 7.5l-4 4 4 4M15 7.5l-4 4 4 4" fill="none" stroke="#555" stroke-width="1.5"/></svg>
      <svg width="23" height="23" viewBox="0 0 23 23" aria-label="Next"><circle cx="11.5" cy="11.5" r="10.5" fill="none" stroke="#777" stroke-width="1.5"/><path d="M8 7.5l4 4-4 4M12 7.5l4 4-4 4" fill="none" stroke="#555" stroke-width="1.5"/></svg>
    </div>

    <section class="card plan">
      <h2>Plan</h2><div class="rule"></div>
      <div class="plan-list">
        <h3>1. Virtual Nursay Planner</h3>
        <p>Layout the nursery of your dreams with just the click of a button! Choose furniture, move it around, then print out your floor plan. Most importantly have fun!</p>
        <h3>2. Wall Decals</h3>
        <p>Wall Art decals are a simple and paint-free way to spice up your nursery. The easy to apply decals can help enhance your nursery theme, or can be used to completely change the look of your room.</p>
      </div>
      <span class="more">MORE</span>
    </section>

    <section class="card shop">
      <h2>Shop</h2><div class="rule"></div>
      <div class="shop-label" style="left:29px;top:123px">Beds &amp;<br>Mattresses</div>
      <div class="thumb" role="img" aria-label="Cot with patterned bedding" style="left:106px;top:108px;background:#d9c7c2"></div>
      <div class="thumb" role="img" aria-label="Bedroom set in lilac tones" style="left:19px;top:164px;background:#b7a3c4"></div>
      <div class="shop-label" style="left:88px;top:175px;text-align:right;width:70px">Bedroom<br>Set Savings</div>
      <div class="shop-label" style="left:31px;top:232px;text-align:center">Bookcases<br>&amp; Storage</div>
      <div class="thumb" role="img" aria-label="White bookcase with storage" style="left:105px;top:213px;background:#e4ddd8"></div>
      <div class="thumb" role="img" aria-label="Pink play kitchen" style="left:19px;top:264px;background:#e6b8c4"></div>
      <div class="shop-label" style="left:85px;top:280px;text-align:center">Kitchens &amp;<br>Play Furniture</div>
      <span class="more">MORE</span>
    </section>

    <section class="card support">
      <h2>Support</h2><div class="rule"></div>
      <div class="support-list">
        <h3>1. Virtual Nursay Planner</h3><p>Lorem ipsum dolor sit amet,<br>consectetur adipiscing elit.</p>
        <h3>2. Assembly Instructions</h3><p>Lorem ipsum dolor sit amet,<br>consectetur adipiscing elit.</p>
        <h3>3. Product Brochures</h3><p>Lorem ipsum dolor sit amet,<br>consectetur adipiscing elit.</p>
        <h3>4. Part Request</h3><p>Lorem ipsum dolor sit amet,</p>
      </div>
      <span class="more">MORE</span>
    </section>

    <section class="card connect">
      <h2>Connect</h2><div class="rule"></div>
      <div class="script" style="top:110px">Visit our Blogs</div>
      <div class="social-box"><span>Pagebook</span><span>Chirpline</span><span>Clipstream</span></div>
      <div class="script" style="top:228px">Subscribe now</div>
      <div class="field" style="top:259px">Enter Your Name</div>
      <div class="field" style="top:284px">Enter Your Email</div>
      <span class="subscribe">Subscribe</span>
      <span class="more">MORE</span>
    </section>

    <div class="card-photo" role="img" aria-label="Black baby carrier" style="left:137px;top:598px;width:86px;height:134px;border-radius:30px 30px 16px 16px;background:linear-gradient(#3a3a3a,#1f1f1f)"></div>
    <div class="card-photo" role="img" aria-label="Green frog toy storage box" style="left:334px;top:598px;width:106px;height:118px;border-radius:40px 40px 20px 20px;background:linear-gradient(#7cc05a,#4f8f38)"></div>
    <div class="card-photo" role="img" aria-label="Cream wardrobe with giraffe decal" style="left:555px;top:614px;width:64px;height:116px;background:linear-gradient(#f2ead3,#e2d6b4)"></div>
    <div class="card-photo" role="img" aria-label="Two children sitting in red and black egg chairs" style="left:727px;top:617px;width:140px;height:116px;border-radius:40px 40px 12px 12px;background:linear-gradient(90deg,#c8372c 0 48%,#2c2c2c 52%)"></div>
  </div>

  <div class="footer">© Cradle Lane 2012-2013<br><a>Privacy Plicy</a> | <a>Terms &amp; Conditions</a></div>
  <div class="footer-social"><span class="dark">Pagebook</span><span class="light">Chirpline</span></div>
</div>
</body>
</html>
```